Window Tinting Website Design

We are working with a Window Tinting company in California. They do commercial, residential, and automotive tint.

Some websites for inspiration:
https://www.velofilmz.com/
https://www.tkglossbay.com/
https://orbishadez.com/

Thank you for taking the time to consider designing a website for us. We are web developers based in Stockton, CA, USA. Most of our projects go through the same process. Understanding this process may help you win a project with us. We custom-code all of our websites in-house. We don’t have any requirements as to what tools you use for your design, but we ask that you follow these guidelines.

IMAGES:
If you use any images or icons in the design, we ask that you have a link to the asset so we can purchase the image/icon. Most of the designs we submit do not have the customer’s images on them unless they have some great images. Be creative; show us the feeling you are trying to portray with your image choices. Use any royalty-free site you choose. We subscribe to Brellix and mainly use their images, but we can purchase images outside of Brellix. PLEASE NOTE: we will not submit designs to clients with watermarks on the images.

FONTS:
We ask that you identify the fonts you’re using in the design. This can be done in a message if you want. We typically use Tarvo Fonts and Brellix Fonts.

CONTENT:
We're always open to different content and ideas. We often submit designs with stock images so the client can see our vision. We typically take pictures after the website launch to use their images with our vision. Lorem Ipsum is fine for paragraphs, but we ask that you make the Headers with correct English. We want to be able to show the vision and identify the sections of the website.

INSPIRATION:
We typically add a couple of links in the brief of websites we like to help you get started in your design.

REVISIONS:
We do not often ask for revisions of the designs unless we see something in the design that may not appeal to the client. If there are slight changes that we want to make, we do that in the development process.

FEEDBACK:
We rarely give feedback on designs during the design process. We are working on many website projects and do not have the time to provide feedback. We usually respond if your request is well thought out and asks specific questions, but a note asking “feedback, please” usually goes unanswered.

```html
<!DOCTYPE html>
<html lang="en">
<head>
<meta charset="utf-8">
<title>Sunvale Window Tinting</title>
<link href="https://fonts.googleapis.com/css2?family=Mulish:wght@400;600;700;800&display=swap" rel="stylesheet">
<style>
:root{
  --red:#c8102e;
  --bg:#232323;
  --bg-dark:#151515;
  --card:#303030;
  --text:#ffffff;
  --muted:#c9c9c9;
  --star:#f2b705;
}
*{box-sizing:border-box;margin:0;padding:0}
html,body{width:1200px;height:5000px;overflow:hidden}
body{background:var(--bg);color:var(--text);font-family:'Mulish',sans-serif}
.page{position:relative;width:1200px;height:5000px}
section,header,footer{position:relative;width:1200px;overflow:hidden}
.accent{color:var(--red)}
.btn{display:inline-block;background:var(--red);color:#fff;font-weight:700;font-size:14px;border-radius:30px;padding:12px 26px;text-decoration:none}
.btn-sm{font-size:12px;padding:10px 22px}
.logo{display:flex;align-items:center;gap:10px;font-weight:800;font-size:19px;color:#fff}
.logo-dot{width:26px;height:26px;border-radius:50%;background:var(--red)}
.photo{position:absolute}

/* hero */
.hero{height:700px;background:#1b1b1b}
.hero-photo{inset:0;background:linear-gradient(100deg,#1a1a1a 0%,#3b3b3b 30%,#a5281c 55%,#d84a22 70%,#5a1a12 88%,#262626 100%)}
.hero-shade{position:absolute;inset:0;background:linear-gradient(180deg,rgba(0,0,0,.75) 0%,rgba(0,0,0,.2) 40%,rgba(0,0,0,.25) 100%)}
.nav{position:absolute;top:22px;left:120px;right:120px;display:flex;align-items:center;justify-content:space-between}
.nav-links{display:flex;gap:44px;font-size:13px;font-weight:600;margin-left:110px}
.hero-copy{position:absolute;left:160px;top:200px;width:560px}
.hero-copy h1{font-size:46px;font-weight:700;line-height:1.22}
.hero-copy p{font-size:13px;line-height:1.6;margin:34px 0 30px;color:#eee}

/* stats */
.stats{height:217px;background:var(--bg-dark);display:flex;justify-content:space-around;padding:62px 150px 0}
.stat{text-align:center}
.stat-num{font-size:44px;font-weight:600}
.stat-label{font-size:18px;font-weight:600;margin-top:14px}

/* services */
.services{height:1283px;padding-top:120px}
.service{position:relative;height:380px}
.service-text{position:absolute;top:55px;width:440px}
.service-text h2{font-size:33px;font-weight:600;margin-bottom:18px}
.service-text p{font-size:13px;line-height:1.7;color:var(--muted);margin-bottom:40px}
.service .photo{top:0;width:440px;height:310px}
.left{left:120px}.right{left:641px}

/* features */
.features{height:215px;background:var(--bg-dark);display:flex;justify-content:space-around;padding:52px 150px 0}
.feature{text-align:center;width:260px}
.feature-icon{width:40px;height:40px;border-radius:50%;background:var(--red);margin:0 auto 18px;display:flex;align-items:center;justify-content:center}
.feature-label{font-size:19px;font-weight:600}

/* process */
.process{height:465px}
.process-text{position:absolute;left:160px;top:115px;width:360px}
.process-text h2{font-size:39px;font-weight:600;margin-bottom:20px}
.process-text p{font-size:13px;line-height:1.7;color:var(--muted)}
.process .photo{left:684px;top:118px;width:440px;height:245px;background:linear-gradient(90deg,#555 0%,#8c8c8c 30%,#4a4a4a 55%,#9a9a9a 80%,#6b6b6b 100%)}
.play{position:absolute;left:858px;top:218px;width:44px;height:44px;border-radius:50%;background:var(--red);display:flex;align-items:center;justify-content:center}

/* works */
.works{height:770px;background:var(--bg-dark);text-align:center}
.section-head h2{font-size:40px;font-weight:600}
.section-head p{font-size:13px;line-height:1.7;color:var(--muted);width:440px;margin:16px auto 0}
.works .section-head{padding-top:60px}
.tabs{display:flex;justify-content:center;gap:22px;font-size:12px;color:var(--muted);margin-top:38px}
.tabs .active{color:#fff;font-weight:700;border-bottom:3px solid var(--red);padding-bottom:8px}
.grid{position:absolute;top:240px;left:0;display:grid;grid-template-columns:repeat(3,400px);grid-template-rows:repeat(2,265px)}

/* cta */
.cta{height:150px;background:var(--bg-dark);display:flex;align-items:center;justify-content:space-between;padding:0 120px 0 163px}
.cta h2{font-size:32px;font-weight:600}

/* testimonials */
.testimonials{height:740px;text-align:center;padding-top:120px}
.cards{display:flex;justify-content:space-between;width:960px;margin:72px auto 60px}
.card{width:287px;height:282px;background:var(--card);border-radius:10px;padding:30px 26px;text-align:left}
.stars{display:flex;gap:4px;margin-bottom:22px}
.card blockquote{font-size:13px;line-height:1.45;color:#f2f2f2;height:118px;border-bottom:1px solid #777}
.person{display:flex;align-items:center;gap:18px;margin-top:22px}
.avatar{width:36px;height:36px;border-radius:50%;background:linear-gradient(135deg,#8a7a6a,#4a4038)}
.person-name{font-size:13px;font-weight:600}
.person-city{font-size:10px;color:#999;margin-top:2px}

/* footer */
.site-footer{height:420px;background:var(--bg-dark)}
.footer-brand{position:absolute;left:160px;top:90px;width:300px}
.footer-brand p{font-size:13px;line-height:1.6;margin-top:34px}
.socials{display:flex;gap:14px;margin-top:40px}
.social{width:38px;height:38px;border-radius:50%;background:#fff;display:flex;align-items:center;justify-content:center}
.social-mark{width:14px;height:14px;border-radius:50%;background:var(--red)}
.footer-col{position:absolute;top:120px}
.footer-col h3{font-size:20px;font-weight:600;margin-bottom:28px}
.footer-col li{list-style:none;font-size:14px;margin-bottom:22px}
.bottom-bar{position:absolute;left:0;bottom:0;width:1200px;height:80px;background:var(--red);display:flex;align-items:center;padding:0 120px 0 160px;font-size:11px;font-weight:700}
.bottom-bar .legal{margin-left:auto;display:flex;gap:76px}
</style>
</head>
<body>
<div class="page">

<header class="hero">
  <div class="photo hero-photo" role="img" aria-label="Red sports coupe with tinted windows on a dark road"></div>
  <div class="hero-shade"></div>
  <nav class="nav">
    <div class="logo"><span class="logo-dot"></span>Sunvale</div>
    <div class="nav-links"><span>Automotive</span><span>Commercial</span><span>Residential</span><span>About us</span></div>
    <a class="btn btn-sm">Get a quote</a>
  </nav>
  <div class="hero-copy">
    <h1>The <span class="accent">automotive</span> window tinting experts</h1>
    <p>Sed ut perspiciatis unde omnis iste natus error sit voluptatem accusantium doloremque laudantium, totam rem aperiam, eaque ipsa quae ab illo inventore veritatis et quasi architecto beatae vitae dicta sunt explicabo.</p>
    <a class="btn">Get a quote</a>
  </div>
</header>

<section class="stats">
  <div class="stat"><div class="stat-num">1200</div><div class="stat-label">Windows tinted</div></div>
  <div class="stat"><div class="stat-num">45</div><div class="stat-label">Years of experience</div></div>
  <div class="stat"><div class="stat-num">2570</div><div class="stat-label">Happy customers</div></div>
</section>

<section class="services">
  <div class="service">
    <div class="service-text left"><h2><span class="accent">Residential</span> Tinting</h2>
      <p>Neque porro quisquam est, qui dolorem ipsum quia dolor sit amet, consectetur, adipisci velit, sed quia non numquam eius modi tempora incidunt ut. labore et dolore magnam aliquam quaerat voluptatem. Excepteur sint occaecat cupidatat non proident.</p>
      <a class="btn btn-sm">Learn more</a></div>
    <div class="photo right" style="background:linear-gradient(160deg,#e4e6e3,#b9bdb8 45%,#4d5048 80%,#2b2b2b)" role="img" aria-label="Bright living room with large tinted windows"></div>
  </div>
  <div class="service">
    <div class="photo left" style="background:linear-gradient(180deg,#dfe6ec 0%,#6d9cc0 35%,#2a5d86 70%,#3b4650 100%)" role="img" aria-label="Glass office towers against a blue sky"></div>
    <div class="service-text" style="left:656px"><h2><span class="accent">Commercial</span> Tinting</h2>
      <p>Neque porro quisquam est, qui dolorem ipsum quia dolor sit amet, consectetur, adipisci velit, sed quia non numquam eius modi tempora incidunt ut. labore et dolore magnam aliquam quaerat voluptatem. Excepteur sint occaecat cupidatat non proident.</p>
      <a class="btn btn-sm">Learn more</a></div>
  </div>
  <div class="service">
    <div class="service-text left"><h2><span class="accent">Automotive</span> Tinting</h2>
      <p>Neque porro quisquam est, qui dolorem ipsum quia dolor sit amet, consectetur, adipisci velit, sed quia non numquam eius modi tempora incidunt ut. labore et dolore magnam aliquam quaerat voluptatem. Excepteur sint occaecat cupidatat non proident.</p>
      <a class="btn btn-sm">Learn more</a></div>
    <div class="photo right" style="background:linear-gradient(180deg,#2f3d25 0%,#4b5a3a 40%,#b4471f 60%,#5a5a55 80%,#3c3c3a)" role="img" aria-label="Orange sports car on a forest road"></div>
  </div>
</section>

<section class="features">
  <div class="feature"><div class="feature-icon"><svg width="18" height="18" viewBox="0 0 24 24" fill="none" stroke="#fff" stroke-width="2"><path d="M3 12V4h8l10 10-8 8z"/><circle cx="7.5" cy="8.5" r="1.5"/></svg></div><div class="feature-label">Lifetime warranty</div></div>
  <div class="feature"><div class="feature-icon"><svg width="18" height="18" viewBox="0 0 24 24" fill="none" stroke="#fff" stroke-width="2"><path d="M12 2v20M17 6H9.5a3.5 3.5 0 0 0 0 7h5a3.5 3.5 0 0 1 0 7H6"/></svg></div><div class="feature-label">Money-back guarantee</div></div>
  <div class="feature"><div class="feature-icon"><svg width="18" height="18" viewBox="0 0 24 24" fill="none" stroke="#fff" stroke-width="2"><circle cx="12" cy="9" r="6"/><path d="M8.5 14 7 22l5-3 5 3-1.5-8"/></svg></div><div class="feature-label">Licensed installers</div></div>
</section>

<section class="process">
  <div class="process-text"><h2>How We <span class="accent">Work</span></h2>
    <p>Lorem ipsum dolor sit amet, consectetur adipiscing elit, sed do eiusmod tempor incididunt ut labore et dolore magna aliqua. Ut enim ad minim veniam, quis nostrud exercitation ullamco laboris nisi ut aliquip ex ea commodo consequat. Duis aute irure dolor in reprehenderit in voluptate velit esse cillum dolore eu fugiat nulla pariatur. Excepteur sint occaecat cupidatat non proident, sunt in culpa qui officia.</p></div>
  <div class="photo" role="img" aria-label="Installers applying film to tall windows, video still"></div>
  <div class="play"><svg width="16" height="16" viewBox="0 0 24 24" fill="none" stroke="#fff" stroke-width="2.5"><path d="M7 4l13 8-13 8z"/></svg></div>
</section>

<section class="works">
  <div class="section-head"><h2><span class="accent">Selected</span> Works</h2>
    <p>Lorem ipsum dolor sit amet, consetetur sadipscing elitr, sed diam nonumy eirmod tempor invidunt ut labore et dolore magna</p></div>
  <div class="tabs"><span class="active">Show all</span><span>Residential</span><span>Commercial</span><span>Automotive</span></div>
  <div class="grid">
    <div style="background:linear-gradient(180deg,#8a8c8e,#6c6e70 45%,#c9cacb 70%,#4a4a4a)" role="img" aria-label="Silver sedan in front of mountains"></div>
    <div style="background:linear-gradient(180deg,#c9a27a,#e9e3da 40%,#a78a6a 75%,#6e5a48)" role="img" aria-label="Kitchen and dining room with wide windows"></div>
    <div style="background:linear-gradient(180deg,#3d86d0,#8fbde0 40%,#5a7a6a 80%,#3d4a3a)" role="img" aria-label="Glass office building with palm trees"></div>
    <div style="background:linear-gradient(180deg,#7a6a55,#5e6a70 40%,#8a9aa0 70%,#3a4a30)" role="img" aria-label="Glass storefront with a wide overhanging roof"></div>
    <div style="background:linear-gradient(180deg,#4a5560,#8a98a0 45%,#6a6258 75%,#d8d0c8)" role="img" aria-label="Bedroom with floor-to-ceiling windows over the bay"></div>
    <div style="background:linear-gradient(180deg,#a67a4a,#d9a86a 35%,#2d6fa0 60%,#b08058 85%)" role="img" aria-label="Blue sports car on a desert road at sunset"></div>
  </div>
</section>

<section class="cta">
  <h2>Want a free personalized quote?</h2>
  <a class="btn btn-sm">Contact us</a>
</section>

<section class="testimonials">
  <div class="section-head"><h2><span class="accent">Happy</span> Customers</h2>
    <p>Lorem ipsum dolor sit amet, consetetur sadipscing elitr, sed diam nonumy eirmod tempor invidunt ut labore et dolore magna</p></div>
  <div class="cards">
    <article class="card">
      <div class="stars"><svg width="100" height="16" viewBox="0 0 100 16" fill="none" stroke="#f2b705" stroke-width="1.2"><g id="st"><path d="M8 1l2 5h5l-4 3 1.6 5L8 11l-4.6 3L5 9 1 6h5z"/></g><use href="#st" x="20"/><use href="#st" x="40"/><use href="#st" x="60"/><use href="#st" x="80"/></svg></div>
      <blockquote>"Lorem ipsum dolor sit amet, consetetur sadipscing elitr, sed diam nonumy eirmod tempor invidunt ut labore et dolore magna aliquyam erat, sed diam voluptua. At vero"</blockquote>
      <div class="person"><div class="avatar"></div><div><div class="person-name">Dario Wells</div><div class="person-city">Stockton, CA</div></div></div>
    </article>
    <article class="card">
      <div class="stars"><svg width="100" height="16" viewBox="0 0 100 16" fill="none" stroke="#f2b705" stroke-width="1.2"><use href="#st"/><use href="#st" x="20"/><use href="#st" x="40"/><use href="#st" x="60"/><use href="#st" x="80"/></svg></div>
      <blockquote>"Lorem ipsum dolor sit amet, consetetur sadipscing elitr, sed diam nonumy eirmod tempor invidunt ut labore et dolore magna aliquyam erat, sed diam voluptua. At vero"</blockquote>
      <div class="person"><div class="avatar"></div><div><div class="person-name">Lena Marsh</div><div class="person-city">Los Angeles, CA</div></div></div>
    </article>
    <article class="card">
      <div class="stars"><svg width="100" height="16" viewBox="0 0 100 16" fill="none" stroke="#f2b705" stroke-width="1.2"><use href="#st"/><use href="#st" x="20"/><use href="#st" x="40"/><use href="#st" x="60"/><use href="#st" x="80"/></svg></div>
      <blockquote>"Lorem ipsum dolor sit amet, consetetur sadipscing elitr, sed diam nonumy eirmod tempor invidunt ut labore et dolore magna aliquyam erat, sed diam voluptua. At vero"</blockquote>
      <div class="person"><div class="avatar"></div><div><div class="person-name">Otis Brandt</div><div class="person-city">Burbank, CA</div></div></div>
    </article>
  </div>
  <a class="btn btn-sm">See more</a>
</section>

<footer class="site-footer">
  <div class="footer-brand">
    <div class="logo"><span class="logo-dot"></span>Sunvale</div>
    <p>Lorem ipsum dolor sit amet, consectetur adipiscing elit, sed do eiusmod tempor incididunt ut labore et dolore magna aliqua.</p>
    <div class="socials">
      <span class="social"><span class="social-mark"></span></span>
      <span class="social"><span class="social-mark"></span></span>
      <span class="social"><span class="social-mark"></span></span>
      <span class="social"><span class="social-mark"></span></span>
      <span class="social"><svg width="16" height="16" viewBox="0 0 24 24" fill="none" stroke="#c8102e" stroke-width="2"><path d="M22 16.9v3a2 2 0 0 1-2.2 2 19.8 19.8 0 0 1-8.6-3.1 19.5 19.5 0 0 1-6-6A19.8 19.8 0 0 1 2.1 4.2 2 2 0 0 1 4.1 2h3a2 2 0 0 1 2 1.7c.1 1 .4 1.9.7 2.8a2 2 0 0 1-.5 2.1L8 9.9a16 16 0 0 0 6 6l1.3-1.3a2 2 0 0 1 2.1-.4c.9.3 1.8.6 2.8.7a2 2 0 0 1 1.8 2z"/></svg></span>
    </div>
  </div>
  <div class="footer-col" style="left:699px"><h3>Services</h3><ul><li>Automotive Tinting</li><li>Commercial Tinting</li><li>Residential Tinting</li></ul></div>
  <div class="footer-col" style="left:945px"><h3>Resources</h3><ul><li>About us</li><li>Blog</li><li>FAQs</li></ul></div>
  <div class="bottom-bar"><span>© 2023 Sunvale Window Tinting. All Rights Reserved.</span><span class="legal"><span>Privacy Policy</span><span>Terms of Service</span></span></div>
</footer>

</div>
</body>
</html>
```